App design for Monitoring/Notifying Patient's Medication

Design of UX for an Android App that helps patients with medications.

Patient should be able to interact with the App to inform that they have taken the medication (tablets and injections) at proper times.
Ability in App to notify the patient for taking medicines or injections at the proper times.
Medicines and injections to be taken multiple times a day.
Notifications can be visual and audio. Audio may include name and dosage info also.

App requirements
Ability for patient to interact with app to inform that medicine and/or injection has been taken.
Ability to show visual/audio notifications at scheduled times if patient has not taken medicine or injection.
Audio may contain name and dosage of medicine.
In order to increase the use of App, please suggest how to add a rewards section. High level intent is to reward patients who have been taking medications as prescribed for a month.
Menu button at the top which will have 3 action buttons:
1- Home : on click of which the user is back on the landing/notification page.
2-On click of which this will lead the user to a details screen where he can view his medication details as to what all medicines and injections he is taking along with the schedules and the next upcoming notification. This page is entirely read only. It may have a button to help the user go back to the landing page.
3-On click of which, this will show a history of his actions taken in the last 30 days, if the user has pushed the button on notification every time he has consumed the medicine. This page is entirely read only. It may have a button to help the user go back to the landing page.

Thus 3 screens have to be designed:
Home Page
Page for Menu Action button 2
Page for Menu Action button 3

The menu button should be available in all the 3 pages.

The app needs to be simple, friendly and lively so that it ignites an interest in the user to use the app. Please note that many users are illiterate.

It has to be designed only for android phones that will have around 5 inche screen with a resolution between 360 x 640 and 1280 x 720 pixels

Target Market(s)

Patients(most of them are illiterate

Industry/Entity Type

Healthcare

Requirements
Must have
• - best use of screen space. minimum click and scrolls.
• - clean and elegant look.
• - basic font styles
• - bright colors.

```html
<!DOCTYPE html>
<html lang="en">
<head>
<meta charset="utf-8">
<title>dosely – medication reminder home screen</title>
<link rel="stylesheet" href="https://fonts.googleapis.com/css2?family=Raleway:wght@300;400;500;600;700;800&display=swap">
<style>
  :root {
    --backdrop: #6f7c8a;
    --sky: #8ec0f4;
    --sky-deep: #7fb3ec;
    --white: #ffffff;
    --mint: #4fd08f;
    --mint-dark: #2fae6e;
    --cobalt: #4a80d8;
    --future: #d9dadb;
    --future-line: #c7c8ca;
    --grid-line: #9a9a9a;
    --hour-band: #8a8a8a;
    --day-band: #6c6c6c;
    --muted: #b5b5b5;
    --reward: #f26b1d;
  }
  * { box-sizing: border-box; margin: 0; padding: 0; }
  html, body { width: 1200px; height: 1000px; overflow: hidden; }
  body {
    background: var(--backdrop);
    font-family: "Raleway", "Helvetica Neue", Arial, sans-serif;
    position: relative;
  }
  .app-screen {
    position: absolute;
    left: 250px; top: 140px;
    width: 400px; height: 720px;
    background: var(--white);
    overflow: hidden;
    box-shadow: 0 20px 50px rgba(0,0,0,.25);
  }
  .reminder-header {
    position: absolute; left: 0; top: 0;
    width: 400px; height: 300px;
    background: var(--sky);
  }
  .menu-button {
    position: absolute; right: 28px; top: 30px;
    width: 30px; height: 24px;
    display: flex; flex-direction: column; justify-content: space-between;
  }
  .menu-button span { display: block; height: 4px; border-radius: 2px; background: var(--white); }
  .medicine-badge {
    position: absolute; left: 34px; top: 80px;
    width: 124px; height: 124px; border-radius: 50%;
    background: var(--white);
    display: flex; align-items: center; justify-content: center;
  }
  .due-label {
    position: absolute; left: 180px; top: 92px;
    color: #d6e9ff; font-size: 14px; font-weight: 400;
    display: flex; align-items: center; gap: 6px;
  }
  .medicine-name {
    position: absolute; left: 180px; top: 114px;
    color: var(--white); font-size: 34px; font-weight: 600; letter-spacing: .2px;
  }
  .medicine-dose {
    position: absolute; left: 182px; top: 160px;
    color: var(--white); font-size: 15px; font-weight: 400; line-height: 19px;
  }
  .take-slider {
    position: absolute; left: 32px; top: 228px;
    width: 336px; height: 46px; border-radius: 23px;
    background: var(--white);
    box-shadow: inset 0 0 0 3px #e6eef7;
  }
  .take-slider .later {
    position: absolute; left: 22px; top: 12px;
    color: var(--muted); font-size: 19px; font-weight: 300;
  }
  .take-slider .take-knob {
    position: absolute; left: 128px; top: 5px;
    width: 96px; height: 36px; border-radius: 18px;
    background: var(--mint); color: var(--white);
    font-size: 21px; font-weight: 600;
    display: flex; align-items: center; justify-content: center; gap: 6px;
  }
  .take-slider .hint {
    position: absolute; left: 234px; top: 9px;
    color: var(--muted); font-size: 20px; font-weight: 600; letter-spacing: 4px;
  }
  .schedule-grid { position: absolute; left: 0; top: 300px; }
  .schedule-grid text { font-family: "Raleway", Arial, sans-serif; }
</style>
</head>
<body>

<main class="app-screen">
  <section class="reminder-header">
    <div class="menu-button" aria-label="Menu"><span></span><span></span><span></span></div>

    <div class="medicine-badge">
      <svg width="66" height="40" viewBox="0 0 66 40" aria-hidden="true">
        <ellipse cx="33" cy="22" rx="32" ry="17" fill="#3d6fc4"/>
        <ellipse cx="33" cy="18" rx="32" ry="17" fill="var(--cobalt)"/>
        <path d="M30 6 L36 20" stroke="#fff" stroke-width="4" stroke-linecap="round"/>
      </svg>
    </div>

    <p class="due-label">
      <svg width="22" height="24" viewBox="0 0 22 24" aria-hidden="true">
        <rect x="8" y="0" width="6" height="3" rx="1" fill="#d6e9ff"/>
        <circle cx="11" cy="14" r="8.5" fill="none" stroke="#d6e9ff" stroke-width="2.5"/>
        <path d="M11 9 V14 H15" fill="none" stroke="#d6e9ff" stroke-width="2.2" stroke-linecap="round"/>
      </svg>
      It is time to take
    </p>
    <h1 class="medicine-name">Rifampicin</h1>
    <p class="medicine-dose">1 Filmtablette<br>15 mg</p>

    <div class="take-slider">
      <span class="later">later</span>
      <span class="take-knob">take <svg width="10" height="14" viewBox="0 0 10 14" aria-hidden="true"><path d="M2 2 L8 7 L2 12" fill="none" stroke="#fff" stroke-width="2.6" stroke-linecap="round"/></svg></span>
      <span class="hint">› ›</span>
    </div>
  </section>

  <svg class="schedule-grid" width="400" height="420" viewBox="0 0 400 420" aria-label="Weekly medication schedule">
    <defs>
      <symbol id="capsule" viewBox="0 0 42 16">
        <rect x="1" y="1" width="40" height="14" rx="7" fill="currentColor"/>
        <rect x="20" y="1" width="2" height="14" fill="#ffffff" opacity=".55"/>
      </symbol>
      <symbol id="tablet" viewBox="0 0 22 22">
        <circle cx="11" cy="11" r="10" fill="currentColor"/>
        <path d="M9 4 L12 11" stroke="#ffffff" stroke-width="2.4" stroke-linecap="round"/>
      </symbol>
      <symbol id="syringe" viewBox="0 0 52 18">
        <rect x="2" y="3" width="32" height="12" rx="3" fill="currentColor"/>
        <path d="M8 3 V9 M14 3 V9 M20 3 V9 M26 3 V9" stroke="#ffffff" stroke-width="1.6"/>
        <rect x="34" y="7" width="16" height="3" rx="1.5" fill="currentColor"/>
        <circle cx="50" cy="8.5" r="2.5" fill="currentColor"/>
      </symbol>
    </defs>

    <!-- hour rail -->
    <rect x="0" y="0" width="22" height="420" fill="var(--hour-band)"/>

    <!-- future cells -->
    <rect x="172" y="120" width="76" height="240" fill="var(--future)"/>
    <rect x="248" y="0" width="152" height="360" fill="var(--future)"/>

    <!-- current selection -->
    <rect x="178" y="44" width="64" height="32" fill="var(--cobalt)"/>

    <!-- grid lines -->
    <g stroke="var(--grid-line)" stroke-width="1">
      <path d="M22 40 H400 M22 80 H400 M22 120 H400 M22 160 H400 M22 200 H400 M22 240 H400 M22 280 H400 M22 320 H400"/>
      <path d="M97 0 V360 M172 0 V360 M248 0 V360 M324 0 V360"/>
    </g>
    <g stroke="var(--future-line)" stroke-width="1">
      <path d="M248 40 H400 M248 80 H400"/>
    </g>

    <!-- pointer from reminder to current slot -->
    <path d="M194 0 L210 16 L226 0 Z" fill="var(--sky)"/>

    <!-- hour labels -->
    <g fill="#ffffff" font-size="10" font-weight="600" text-anchor="middle">
      <text x="11" y="24">6</text>
      <text x="11" y="64">8</text>
      <text x="11" y="104">10</text>
      <text x="11" y="144">12</text>
      <text x="11" y="184">14</text>
      <text x="11" y="224">16</text>
      <text x="11" y="264">18</text>
      <text x="11" y="304">20</text>
      <text x="11" y="344">22</text>
    </g>

    <!-- column 1 (taken) -->
    <g color="var(--mint)">
      <use href="#capsule" x="38" y="52" width="42" height="16"/>
      <use href="#tablet" x="48" y="88" width="22" height="22"/>
      <use href="#syringe" x="34" y="131" width="52" height="18"/>
      <use href="#capsule" x="38" y="252" width="42" height="16"/>
      <use href="#capsule" x="38" y="292" width="42" height="16"/>
    </g>

    <!-- column 2 (taken / missed) -->
    <g color="var(--mint)">
      <use href="#capsule" x="113" y="52" width="42" height="16"/>
      <use href="#tablet" x="123" y="68" width="22" height="22"/>
      <use href="#tablet" x="123" y="96" width="22" height="22"/>
      <use href="#capsule" x="113" y="252" width="42" height="16"/>
    </g>
    <use href="#capsule" x="113" y="212" width="42" height="16" color="#b9b9b9"/>

    <!-- column 3 (today) -->
    <use href="#capsule" x="189" y="12" width="42" height="16" color="var(--mint)"/>
    <use href="#tablet" x="199" y="49" width="22" height="22" color="#ffffff"/>
    <use href="#syringe" x="184" y="90" width="52" height="18" color="#c9c9c9"/>

    <!-- upcoming days -->
    <g color="#ffffff">
      <use href="#capsule" x="265" y="12" width="42" height="16"/>
      <use href="#tablet" x="275" y="34" width="22" height="22"/>
      <use href="#tablet" x="275" y="62" width="22" height="22"/>
      <use href="#capsule" x="265" y="212" width="42" height="16"/>
      <use href="#capsule" x="265" y="232" width="42" height="16"/>
      <use href="#capsule" x="341" y="12" width="42" height="16"/>
      <use href="#tablet" x="351" y="34" width="22" height="22"/>
      <use href="#tablet" x="351" y="62" width="22" height="22"/>
      <use href="#capsule" x="341" y="212" width="42" height="16"/>
      <use href="#capsule" x="341" y="232" width="42" height="16"/>
    </g>

    <!-- day bar -->
    <rect x="22" y="360" width="378" height="60" fill="var(--day-band)"/>
    <g stroke="#8a8a8a"><path d="M97 360 V420 M172 360 V420 M248 360 V420 M324 360 V420"/></g>

    <!-- reward day -->
    <g class="reward-day">
      <g stroke="var(--reward)" stroke-width="2" stroke-linecap="round">
        <path d="M134 340 V348 M120 344 L125 351 M148 344 L143 351 M112 354 L119 357 M156 354 L149 357"/>
      </g>
      <circle cx="134" cy="376" r="17" fill="var(--reward)"/>
      <path d="M134 365 L137.2 372.4 L145 373 L139 378 L141 386 L134 381.6 L127 386 L129 378 L123 373 L130.8 372.4 Z" fill="#ffffff"/>
      <text x="134" y="410" fill="#ffffff" font-size="10" text-anchor="middle">Mar 14</text>
    </g>

    <g fill="#ffffff" text-anchor="middle">
      <text x="210" y="388" font-size="16" font-weight="600">Tue</text>
      <text x="210" y="404" font-size="10">Mar 15</text>
      <text x="286" y="388" font-size="16" font-weight="600">Fri</text>
      <text x="286" y="404" font-size="10">Mar 16</text>
      <text x="362" y="388" font-size="16" font-weight="600">Sat</text>
      <text x="362" y="404" font-size="10">Mar 17</text>
    </g>
  </svg>
</main>

<p class="brand-name" style="position:absolute;left:740px;top:410px;color:var(--white);font-size:130px;font-weight:800;line-height:1;letter-spacing:-2px;">dosely</p>

</body>
</html>
```